Design Tweak needed for a current site

Design on top of an existing quiz funnel

Ideally we would like to tweak what we have already built here (moving elements, styles, adding simple elements etc): http://offers.rateplumfinder.com/could-you-cut-your-auto-premium

The flow:
1) User lands on the quiz page
2) User answers X questions and moves through the flow
3) Calculating user results screen
4) User reaches a success screen, and is subsequently redirected

Keys to the design:
1) We need to emphasize the quiz title as that will drive engagement. In this case, this is a quiz to see if you might be eligible to save money on car insurance.

2) At the end of the quiz we need to make it very, very clear that the user is eligible for savings and that in order to complete the process they are being redirected to another page where they need to fill out a form. It is critical that the design communicates this very clearly... We can count down the time left until redirect and we can use any order of elements to make this point. I think our current design does a very bad job of this.

3) We want to have a "calculating" step so that it seems like the page is working in the background

Goals of the design:
1) Polished, high quality experience throughout
2) User is clearly prepared to be redirected to the conversion funnel/landing page at the end
3) User understands the value of completing the quiz

Target Market(s)

designers

Industry/Entity Type

Moving

Number of Pages Required

1 page

Font styles to use
Sans Serif

Colors

Designer to choose colors to be used in the design.

Requirements
Must have
• This quiz funnel is a template so while the current use case is for auto insurance, we would like a design that also would work in other contexts.
Should not have
• We don't want to materially change the core functionality of the quiz itself... redesigning any of the elements or interactions is encouraged though

```html
<!DOCTYPE html>
<html lang="en">
<head>
<meta charset="utf-8">
<title>LumaRate – Car Insurance Quiz</title>
<link rel="stylesheet" href="https://fonts.googleapis.com/css2?family=Montserrat:wght@500;600;700&display=swap">
<style>
  :root {
    --green-dark: #4fab4d;
    --green-light: #6cc868;
    --title-green: #43a15a;
    --indigo: #434ea0;
    --button: #4550a5;
    --muted: #9b9b9b;
    --white: #ffffff;
  }
  * { box-sizing: border-box; margin: 0; padding: 0; }
  html, body {
    width: 1200px;
    height: 675px;
    overflow: hidden;
    background: var(--white);
    font-family: "Montserrat", sans-serif;
  }
  .canvas {
    position: relative;
    width: 1200px;
    height: 675px;
  }
  .site-header {
    position: absolute;
    left: 0; top: 0;
    width: 1200px;
    height: 104px;
    background: radial-gradient(ellipse 700px 300px at 830px 40px, var(--green-light) 0%, var(--green-dark) 100%);
    display: flex;
    align-items: center;
    padding-left: 34px;
  }
  .brand {
    display: flex;
    align-items: center;
    gap: 16px;
  }
  .brand-dot {
    width: 60px;
    height: 60px;
    border-radius: 50%;
    background: var(--white);
  }
  .brand-name {
    color: var(--white);
    font-weight: 600;
    font-size: 54px;
    letter-spacing: -0.01em;
    line-height: 1;
  }
  .quiz-intro {
    position: absolute;
    left: 0; top: 0;
    width: 1200px;
    text-align: center;
  }
  .quiz-label {
    position: absolute;
    left: 0; width: 1200px;
    top: 246px;
    font-size: 62px;
    font-weight: 700;
    color: var(--title-green);
    letter-spacing: 0.04em;
    line-height: 1;
  }
  .quiz-title {
    position: absolute;
    left: 0; width: 1200px;
    top: 324px;
    font-size: 37.5px;
    font-weight: 600;
    color: var(--indigo);
    letter-spacing: 0.05em;
    line-height: 1;
  }
  .quiz-lead {
    position: absolute;
    left: 0; width: 1200px;
    top: 409px;
    font-size: 25px;
    font-weight: 600;
    color: var(--muted);
    letter-spacing: 0.05em;
    line-height: 26px;
  }
  .start-button {
    position: absolute;
    left: 529px;
    top: 515px;
    width: 165px;
    height: 61px;
    border: none;
    border-radius: 8px;
    background: var(--button);
    color: var(--white);
    font-family: "Montserrat", sans-serif;
    font-size: 24px;
    font-weight: 500;
    letter-spacing: 0.06em;
  }
</style>
</head>
<body>
  <div class="canvas">
    <header class="site-header">
      <div class="brand">
        <span class="brand-dot"></span>
        <span class="brand-name">LumaRate</span>
      </div>
    </header>
    <main class="quiz-intro">
      <h2 class="quiz-label">Quiz</h2>
      <h1 class="quiz-title">Are You Overpaying For Car Insurance?</h1>
      <p class="quiz-lead">Take our five question quiz to see if you might be<br>eligible for car insurance savings</p>
      <button class="start-button" type="button">start</button>
    </main>
  </div>
</body>
</html>
```